A land page lead collector for people who want to reduce there postage costs

We are looking to create a single page website landing page to collect leads of people who want to reduce there postage costs.

The form should basically ask:

Name:
Business Name:
Address:
Town:
Post Code:
Email:
Phone:
Letter Volume Per Week:
Parcel Volume Per Week:

We should basically be advertising cheaper postage costs.

We will not be showing prices on this website we will just be collecting the leads.

Our competition website is as follows https://mailfernquest.com

But we are not a online service. This is just a collector to get leads of people who want to save money on there postage costs.
Updates

Target Market(s)

Small and medium sized enterprises

Industry/Entity Type

Advertising

Number of Pages Required

1 page

Colors
ec2027
0356a4

Requirements
Must have
• Form above the fold of the page
Nice to have
• Colour red and blue.
• Parallax design would be nice.

```html
<!DOCTYPE html>
<html lang="en">
<head>
<meta charset="utf-8">
<title>Get Started Now – Reduce Your Postage Costs</title>
<link rel="stylesheet" href="https://fonts.googleapis.com/css2?family=Mulish:wght@400;500;600&family=Fjalla+One&display=swap">
<style>
  :root {
    --red: #ec2027;
    --blue: #0356a4;
    --blue-dark: #02407a;
    --select-blue: #7fa6d6;
    --grey: #d6d6d6;
    --ink: #1e1e1e;
    --caption: #333;
    --white: #ffffff;
  }
  * { box-sizing: border-box; margin: 0; padding: 0; }
  html, body { width: 1159px; height: 1200px; overflow: hidden; }
  body { font-family: "Mulish", "Helvetica Neue", Arial, sans-serif; background: var(--grey); position: relative; }

  .hero { position: absolute; left: 0; top: 0; width: 1159px; height: 629px; }
  .hero-form-side { position: absolute; left: 0; top: 0; width: 619px; height: 629px; background: var(--red); }
  .hero-photo {
    position: absolute; left: 619px; top: 0; width: 540px; height: 629px;
    background: radial-gradient(ellipse at 35% 30%, #6b5a52 0%, #4a403c 45%, #2e2a29 100%);
  }
  .hero-photo::after { content: ""; position: absolute; inset: 0; background: rgba(0,0,0,0.25); }

  .free-badge { position: absolute; left: 95px; top: 0; width: 71px; height: 94px; }
  .free-badge-text { position: absolute; left: 95px; top: 12px; width: 71px; text-align: center; color: #b9cde6; }
  .free-badge-text .small { font-size: 11px; line-height: 14px; font-family: Arial, sans-serif; }
  .free-badge-text .big { font-family: "Fjalla One", sans-serif; font-size: 22px; line-height: 24px; color: #dfe8f4; }

  .mascot {
    position: absolute; left: 84px; top: 296px; width: 164px; height: 246px;
    background: linear-gradient(180deg, #c9955e 0%, #1f5e86 45%, #174a6b 100%);
    border-radius: 40px 40px 16px 16px; opacity: 0.9;
  }

  .form-title { position: absolute; left: 250px; top: 66px; width: 263px; text-align: center; color: var(--white); font-size: 32px; font-weight: 400; white-space: nowrap; }
  .lead-form { position: absolute; left: 250px; top: 124px; width: 263px; }
  .field {
    position: absolute; left: 0; width: 263px; height: 34px; background: var(--white);
    box-shadow: inset 0 3px 0 #f2f2f2; color: #333; font-size: 12px; padding-left: 12px; line-height: 34px;
  }
  .field.select::after { content: ""; position: absolute; right: 0; top: 0; width: 29px; height: 34px; background: var(--select-blue); }
  .field .chev { position: absolute; right: 9px; top: 13px; z-index: 1; }
  .submit {
    position: absolute; left: 2px; top: 368px; width: 212px; height: 52px; background: var(--blue);
    border-bottom: 4px solid var(--blue-dark); color: var(--white); font-size: 17px; text-align: center; line-height: 48px;
  }

  .hero-message { position: absolute; left: 696px; top: 276px; width: 350px; color: var(--white); font-size: 30px; line-height: 38.5px; font-weight: 400; z-index: 1; }

  .social { position: absolute; top: 32px; left: 961px; display: flex; gap: 4px; z-index: 1; }
  .social-item { width: 32px; height: 32px; border: 1.5px solid var(--white); border-radius: 50%; color: var(--white); font-size: 6px; display: flex; align-items: center; justify-content: center; text-align: center; }

  .intro { position: absolute; left: 150px; top: 692px; width: 859px; text-align: center; color: var(--ink); font-size: 28.5px; line-height: 35px; }

  .feature { position: absolute; top: 806px; width: 212px; }
  .feature-box { width: 212px; height: 172px; background: var(--red); display: flex; align-items: center; justify-content: center; }
  .feature-caption { margin-top: 18px; text-align: center; color: var(--caption); font-size: 14px; line-height: 18px; }

  .footer { position: absolute; left: 0; top: 1110px; width: 1159px; height: 90px; background: var(--blue); color: var(--white); font-family: Arial, sans-serif; font-size: 14px; text-align: center; line-height: 90px; }
</style>
</head>
<body>
<section class="hero">
  <div class="hero-form-side">
    <svg class="free-badge" viewBox="0 0 71 94"><path d="M0 0H71V94L35.5 84L0 94Z" fill="#0356a4"/></svg>
    <div class="free-badge-text">
      <div class="small">100%</div>
      <div class="big">FREE</div>
      <div class="small">Soon</div>
    </div>
    <div class="mascot" role="img" aria-label="Cartoon businessman in a blue suit giving a thumbs up"></div>

    <h1 class="form-title">Get Started Now</h1>
    <div class="lead-form">
      <div class="field" style="top:0">Name</div>
      <div class="field" style="top:39px">Business Name</div>
      <div class="field" style="top:78px">Address</div>
      <div class="field" style="top:118px">Post Code</div>
      <div class="field select" style="top:158px">Town<svg class="chev" width="10" height="7" viewBox="0 0 10 7"><path d="M1 1l4 4 4-4" stroke="#fff" stroke-width="2" fill="none"/></svg></div>
      <div class="field" style="top:197px">Phone</div>
      <div class="field" style="top:237px">Email</div>
      <div class="field select" style="top:277px">Letter Volume Per Week<svg class="chev" width="10" height="7" viewBox="0 0 10 7"><path d="M1 1l4 4 4-4" stroke="#fff" stroke-width="2" fill="none"/></svg></div>
      <div class="field select" style="top:317px">Parcel Volume Per Week<svg class="chev" width="10" height="7" viewBox="0 0 10 7"><path d="M1 1l4 4 4-4" stroke="#fff" stroke-width="2" fill="none"/></svg></div>
      <div class="submit">Submit Now</div>
    </div>
  </div>

  <div class="hero-photo" role="img" aria-label="Woman smiling as she unpacks a parcel filled with bubble wrap"></div>
  <div class="social">
    <div class="social-item">Friendline</div>
    <div class="social-item">Workring</div>
    <div class="social-item">Chirpnet</div>
  </div>
  <p class="hero-message">We just collect leads of people who want to reduce there postage costs.</p>
</section>

<p class="intro">Lorem ipsum dolor sit amet, consectetur adipisicing elit, sed do eiusmod tempor incididunt ut labore et dolore magna aliqua.</p>

<div class="feature" style="left:226px">
  <div class="feature-box">
    <svg width="70" height="90" viewBox="0 0 70 90"><path d="M8 4c6-4 10-4 12 0l8 14c2 4 0 7-4 9l-4 2c2 14 12 30 24 38l4-3c4-3 7-2 9 1l10 13c2 4 0 7-6 10-6 3-14 2-22-6C22 66 6 40 2 20 0 12 2 8 8 4z" fill="#fff"/></svg>
  </div>
  <p class="feature-caption">Lorem ipsum dolor sit amet,<br>consectetur adipisicing elit,<br>sed do eiusmod</p>
</div>
<div class="feature" style="left:474px">
  <div class="feature-box">
    <svg width="90" height="82" viewBox="0 0 90 82"><path d="M2 0V80H90" stroke="#fff" stroke-width="3" fill="none"/><rect x="11" y="24" width="16" height="50" fill="#fff"/><rect x="31" y="2" width="16" height="72" fill="#fff"/><rect x="51" y="40" width="16" height="34" fill="#fff"/><rect x="71" y="62" width="16" height="12" fill="#fff"/></svg>
  </div>
  <p class="feature-caption">Lorem ipsum dolor sit amet,<br>consectetur adipisicing elit,<br>sed do eiusmod</p>
</div>
<div class="feature" style="left:722px">
  <div class="feature-box">
    <svg width="104" height="58" viewBox="0 0 104 58"><rect x="0" y="0" width="104" height="58" fill="#fff"/><rect x="8" y="8" width="88" height="42" fill="#ec2027"/><circle cx="52" cy="29" r="19" fill="#fff"/><circle cx="22" cy="29" r="5" fill="#fff"/><circle cx="82" cy="29" r="5" fill="#fff"/><text x="52" y="39" text-anchor="middle" font-family="Arial, sans-serif" font-weight="bold" font-size="28" fill="#ec2027">$</text></svg>
  </div>
  <p class="feature-caption">Lorem ipsum dolor sit amet,<br>consectetur adipisicing elit,<br>sed do eiusmod</p>
</div>

<footer class="footer">Copyright © 2015</footer>
</body>
</html>
```